Cloud Software Services Business Card Design Challenge

We are seeking a fresh and creative business card design that aligns with the brand identity of a startup cloud software services company. As a company specializing in advanced cloud solutions, we want these business cards to reflect our technological leadership and professionalism, helping us stand out in business communications and emphasize our core values.

About Us: We are dedicated to supporting the digital transformation of interior design companies through efficient, reliable, and innovative cloud software services. Our goal is to provide the best technological solutions to drive continuous growth and success for our clients.

Design Requirements:

• Colors: We have not yet established a final color scheme, so please do not feel constrained by the current logo colors. The logo colors can be adjusted according to the overall design. We would like you to choose colors based on your design concept, considering a minimalist, professional, and high-end palette. While many tech companies use a lot of blue, we prefer to avoid this common approach, so feel free to explore other color options.

• Style: The business card design should be modern, clean, and professional, reflecting our technological leadership and innovation capabilities. The design should have a strong visual impact and showcase our expertise in cloud technology.

• Visual Elements: We want the overall feel to be simple and clean. Consider incorporating technology-inspired design elements, such as sleek lines or geometric shapes, to enhance our brand's modern tech image.

• Final Design: The business card should have clear readability and a logical layout, and be suitable for various physical media. The design should accurately reflect our company's professional image and innovative capabilities in the cloud software services field.

• Information Layout: The card should include the following details (we will provide the details for 1 name after selecting the winner and ask the designer to provide four final information of the same design—
1. Chinese version with the job title
2. Chinese version without the job title
3. English version with the job title
4. English version without the job title
o Name
o Job Title
o Company Name and Address
o Tax ID Number
o Phone Number
o Email Address
o Company Website URL
o QR Code

We look forward to seeing how your design can showcase our excellence and professionalism in the cloud software services industry. We hope your creativity will help us effectively communicate our brand values!

Target Market(s)

Interior Design Companies

Contact Information for Business Card

The card should include the following details (we will provide the details for 1 name after selecting the winner and ask the designer to provide four final information of the same design— 1. Chinese version with the job title 2. Chinese version without the job title 3. English version with the job title 4. English version without the job title o Name o Job Title o Company Name and Address o Tax ID Number o Phone Number o Email Address o Company Website URL o QR Code

Colors
0054AA
0677BA
7BADD7
CADEEF
E8F1F8
0094D4
00A9DD
6FCCEA
C7EBF8
E9F6FB
00AB8E
00BBA5
67D7C9
C6EFE9
E9F9F6
FFC000
F8CF3A
FAE287
FDF2CF
FEFAEE
F0912C
F2A743
F7CA91
FBE8D2
FDF5EE
EE7325
F08F49
F5BC92
FAE3D3
FDF4ED
A7469A
B969AE
D3A5CF
EDDBEB
F8F0F9
6B429C
8869AF
B7A5CE
E3DAEB
F3F0F8

```html
<!DOCTYPE html>
<html lang="en">
<head>
<meta charset="utf-8">
<title>Nimbora Business Card</title>
<link href="https://fonts.googleapis.com/css2?family=Michroma&family=Arimo:wght@400;500&display=swap" rel="stylesheet">
<style>
  :root {
    --stage: #3b3b3d;
    --paper: #f7f7f5;
    --ink: #2b2b2b;
    --ink-soft: #4a4a4a;
    --accent: #e8521f;
    --edge: #c9260f;
    --night: #262626;
    --night-pattern-a: #1c1c1c;
    --night-pattern-b: #3a3a3a;
    --rule: #9a9a9a;
  }
  * { box-sizing: border-box; margin: 0; padding: 0; }
  html, body { width: 1200px; height: 1108px; overflow: hidden; }
  body {
    background: var(--stage);
    font-family: "Arimo", Arial, sans-serif;
    position: relative;
  }
  .card {
    position: absolute;
    left: 160px;
    width: 880px;
    height: 503px;
    border-bottom: 4px solid var(--edge);
    overflow: hidden;
  }
  .card--front { top: 40px; background: var(--paper); }
  .card--back { top: 565px; background: var(--night); }

  .brand {
    display: flex;
    align-items: center;
    gap: 14px;
    font-family: "Michroma", sans-serif;
    letter-spacing: 4px;
    font-size: 30px;
  }
  .brand__dot {
    width: 14px; height: 14px; border-radius: 50%;
    background: var(--accent);
  }
  .card--front .brand {
    position: absolute; left: 90px; top: 215px; color: var(--ink);
  }
  .card--back .brand {
    position: absolute; right: 70px; bottom: 70px; color: #ffffff;
  }

  .divider {
    position: absolute; left: 468px; top: 120px;
    width: 1px; height: 270px; background: var(--rule);
  }

  .contact { position: absolute; left: 510px; top: 118px; color: var(--ink-soft); }
  .contact__name {
    font-family: "Michroma", sans-serif;
    color: var(--accent);
    font-size: 27px;
    letter-spacing: 3px;
    line-height: 1.1;
  }
  .contact__title { font-size: 17px; margin-top: 4px; }
  .contact__address { font-size: 18px; margin-top: 26px; line-height: 1.35; }
  .contact__tax { font-size: 18px; margin-top: 4px; }
  .contact__tax-label { color: var(--accent); }
  .contact__list { list-style: none; margin-top: 14px; font-size: 18px; line-height: 1.45; }
  .contact__list li { display: flex; align-items: center; gap: 12px; }
  .contact__list svg { width: 16px; height: 16px; fill: var(--accent); flex: none; }

  .pattern-field {
    position: absolute; inset: 0;
    background: linear-gradient(120deg, var(--night-pattern-a) 0%, var(--night) 50%, var(--night-pattern-b) 100%);
  }
</style>
</head>
<body>
  <section class="card card--front">
    <div class="brand"><span class="brand__dot"></span><span>NIMBORA</span></div>
    <div class="divider"></div>
    <div class="contact">
      <h1 class="contact__name">CLARA HALE</h1>
      <p class="contact__title">President</p>
      <p class="contact__address">1420 Cedar Row<br>Halden, Canada 20418</p>
      <p class="contact__tax"><span class="contact__tax-label">Tax ID :</span> 318-52-4071</p>
      <ul class="contact__list">
        <li><svg viewBox="0 0 16 16"><path d="M3 1l3 3-1.5 2c1 2 3 4 5 5l2-1.5 3 3-2 2C7 14 2 9 1 3z"/></svg>604-219-5830</li>
        <li><svg viewBox="0 0 16 16"><path d="M1 3h14v10H1z M2 4l6 5 6-5" fill="none" stroke="#e8521f" stroke-width="1.6"/></svg>hello@nimbora.com</li>
        <li><svg viewBox="0 0 16 16"><circle cx="8" cy="8" r="7"/></svg>www.nimbora.com</li>
      </ul>
    </div>
  </section>

  <section class="card card--back">
    <div class="pattern-field" role="img" aria-label="Repeating tone-on-tone brand pattern across the dark card back"></div>
    <div class="brand"><span class="brand__dot"></span><span>NIMBORA</span></div>
  </section>
</body>
</html>
```